Water Board Political Campaign Sign

1. Simple elegant clean design highly visible possibly with white text and blue and green as accent colors and water theme as design element
2. Clean sans-serif fonts like Helvetica or Arial
3. Wording on sign: Dan (small font) Prewitt (largest font possible) & Margaret (small font) Castellow (largest font possible) but please do not use all caps for names.
for Marrow Hollow Water District Directors (slightly smaller font)
Leading with Experience, Committed to a Sustainable Future
Vote Nov. 5 ( small font size)
In very small font at bottom of sign FPPC#2836094
4. We need two yard signs--one medium sign about 18" x 24" and
another larger sign about 48" x 96"

Target Market(s)

Mixed township 60% Democrat

Industry/Entity Type

Water

Font styles to use
Sans Serif

Requirements
Must have
• Water theme

```html
<!DOCTYPE html>
<html lang="en">
<head>
<meta charset="utf-8">
<title>Prewitt &amp; Castellow Yard Sign</title>
<link rel="stylesheet" href="https://fonts.googleapis.com/css2?family=Montserrat:wght@500;600;700;800&display=swap">
<style>
  :root {
    --navy: #263f78;
    --green: #3e8a4a;
    --water: #5aa6d6;
    --white: #ffffff;
    --backdrop: #eef1f4;
    --ink: #263f78;
  }
  * { margin: 0; padding: 0; box-sizing: border-box; }
  html, body {
    width: 1200px; height: 1200px; overflow: hidden;
    background: var(--backdrop);
  }
  body {
    display: flex; align-items: center; justify-content: center;
    font-family: "Montserrat", Arial, sans-serif;
  }
  .yard-sign {
    width: 1100px; height: 900px;
    background: var(--white);
    padding: 30px 32px 28px;
    display: flex; flex-direction: column;
    box-shadow: 0 6px 24px rgba(0,0,0,0.12);
  }
  .band { background: var(--green); flex: none; }
  .band--top { height: 30px; }
  .name-panel {
    background: var(--navy);
    height: 470px;
    flex: none;
    display: flex; flex-direction: column; align-items: center; justify-content: center;
    color: var(--white);
    text-align: center;
  }
  .candidates {
    font-weight: 800;
    line-height: 1.05;
  }
  .candidate { display: block; white-space: nowrap; }
  .first-name {
    font-size: 38px;
    font-weight: 600;
    margin-right: 16px;
    vertical-align: baseline;
  }
  .last-name { font-size: 118px; letter-spacing: 0; }
  .amp { color: var(--green); font-size: 118px; margin-left: 14px; }
  .office {
    margin-top: 26px;
    font-weight: 500;
    font-size: 30px;
    letter-spacing: 2px;
    line-height: 1.35;
  }
  .office .rule-line {
    display: flex; align-items: center; justify-content: center; gap: 32px;
  }
  .office .rule-line::before, .office .rule-line::after {
    content: ""; width: 44px; height: 2px; background: var(--white);
  }
  .wave-edge { display: block; width: 100%; height: 44px; flex: none; }
  .message {
    flex: 1;
    display: flex; flex-direction: column; align-items: center; justify-content: center;
    color: var(--ink);
    text-align: center;
  }
  .tagline {
    font-weight: 700; font-size: 32px; line-height: 1.35;
  }
  .vote-date {
    margin-top: 16px;
    font-weight: 800; font-size: 40px; letter-spacing: 2px; color: var(--green);
  }
  .band--foot {
    height: 40px;
    display: flex; align-items: center; justify-content: space-between;
    padding: 0 16px;
    color: var(--white);
  }
  .disclosure { font-size: 11px; font-weight: 500; letter-spacing: 2px; text-transform: uppercase; }
  .fppc { font-size: 13px; font-weight: 700; letter-spacing: 1px; }
</style>
</head>
<body>
  <main class="yard-sign">
    <div class="band band--top"></div>
    <section class="name-panel">
      <h1 class="candidates">
        <span class="candidate"><span class="first-name">Dan</span><span class="last-name">Prewitt</span><span class="amp">&amp;</span></span>
        <span class="candidate"><span class="first-name">Margaret</span><span class="last-name">Castellow</span></span>
      </h1>
      <p class="office">
        <span class="rule-line">for Marrow Hollow</span>
        Water District Directors
      </p>
    </section>
    <svg class="wave-edge" viewBox="0 0 1036 44" preserveAspectRatio="none" aria-hidden="true">
      <path d="M0 0 H1036 V18 C975 40 915 40 863 22 C811 4 751 4 690 22 C630 40 570 40 518 22 C466 4 406 4 345 22 C285 40 225 40 173 22 C121 4 61 4 0 22 Z" fill="var(--green)"/>
      <path d="M0 32 C61 14 121 14 173 32 C225 44 285 44 345 32 C406 14 466 14 518 32 C570 44 630 44 690 32 C751 14 811 14 863 32 C915 44 975 44 1036 32" fill="none" stroke="var(--water)" stroke-width="4"/>
    </svg>
    <section class="message">
      <p class="tagline">Leading with Experience,<br>Committed to a Sustainable Future</p>
      <p class="vote-date">Vote Nov. 5</p>
    </section>
    <footer class="band band--foot">
      <span class="disclosure">Paid for by the committee</span>
      <span class="fppc">FPPC#2836094</span>
    </footer>
  </main>
</body>
</html>
```